Brindle Works Australia Website

Brindle Works Australia (BWA) is a Industrial, Mining & Transport Services provider in Australia. We require a website that is both pc and mobile freindly. The website will be used to both present our company services and give us exposure in a crowded market. The main page of the website will have a snapshot of who BWA is and its from this page that the user can click to enter the area of interest ie. Industrial, Mining and Transport. A disticted logo can be used to indicate the area in question.<br/>Within the industrial, Mining and the Transport services pages will need list and description of services that are provided, current customer lists and news pages.<br/>The website will need a contacts page so prospective customers can get in contact with BWA.<br/>The website design will require a user freindly back end so future updates and ammendments can be carriedout by less experienced people within the BWA business.

Target Market(s)

Industrial, Mining and Transport Services provider markets

Coding

Coded - Design and coding required

Number of Pages Required

5+ page

Font styles to use
Sans Serif

Colors
00a990

Requirements
Must have
• Ability to build servises with in services. because the main service area is only the main service with in each service group there is alot of smaller services / tasks.
• Key wording for easy seach engine capabilities. The website will need to be search engine freindly.

```html
<!DOCTYPE html>
<html lang="en">
<head>
<meta charset="utf-8">
<title>Brindle Works Australia – Mining &amp; Transport Services</title>
<link href="https://fonts.googleapis.com/css2?family=Lato:ital,wght@0,400;0,700;0,900;1,400&family=Ubuntu:wght@500;700&family=Oswald:wght@500&display=swap" rel="stylesheet">
<style>
:root{
  --green:#0b6a36;
  --green-dark:#075029;
  --ink:#111;
  --text:#333;
  --muted:#666;
  --footer:#0d0d0d;
  --paper:#ececec;
}
*{box-sizing:border-box;margin:0;padding:0}
html,body{width:1200px;height:3563px;overflow:hidden}
body{font-family:'Lato',sans-serif;color:var(--text);background:#fff;position:relative}
h1,h2,h3{font-family:'Ubuntu',sans-serif;font-weight:700}
.abs{position:absolute}

/* hero */
.hero{position:absolute;left:0;top:0;width:1200px;height:532px;
  background:linear-gradient(100deg,#6f8fa3 0%,#3f6d86 25%,#8ea3a8 45%,#e8dcc0 65%,#f0e2c4 100%)}
.hero-road{position:absolute;left:0;bottom:0;width:1200px;height:170px;
  background:linear-gradient(180deg,rgba(190,160,120,0) 0%,#b79877 60%,#8f7257 100%)}
.hero-truck{position:absolute;left:90px;top:90px;width:520px;height:380px;border-radius:20px;
  background:radial-gradient(ellipse at 45% 45%,#2f7d96 0%,#2a5466 45%,rgba(50,70,80,0) 75%)}
.topbar{position:absolute;left:250px;top:11px;width:704px;height:38px;display:flex}
.brand{background:#fff;display:flex;align-items:center;gap:8px;padding:0 10px;width:130px;height:38px}
.brand-mark{width:14px;height:14px;background:var(--green)}
.brand-name{font-family:'Lato',sans-serif;font-weight:900;color:var(--green);font-size:10px;line-height:11px;text-transform:uppercase}
.nav{flex:1;background:var(--green);border-radius:0 26px 26px 0;display:flex;align-items:center;justify-content:space-between;padding:0 40px 0 10px}
.nav-tag{color:#fff;font-weight:900;font-size:10px;line-height:10px;text-transform:uppercase}
.nav ul{list-style:none;display:flex;gap:16px}
.nav li{color:#fff;font-size:11px;font-weight:700}
.hero-copy{position:absolute;left:632px;top:193px;width:330px}
.hero-copy h1{font-size:34px;line-height:40px;color:#151515;text-transform:uppercase}
.hero-copy h1 span{color:var(--green)}
.hero-copy p{font-size:17px;font-weight:700;color:#111;margin-top:14px;line-height:22px}
.btn-dark{display:inline-block;background:#111;color:#fff;font-size:10px;font-weight:700;padding:9px 15px;margin-top:18px}

/* services */
.services-head{position:absolute;top:568px;width:1200px;text-align:center}
.services-head .kicker{font-family:'Ubuntu',sans-serif;font-weight:700;font-size:17px;color:#111}
.services-head h2{font-size:29px;color:var(--green);text-transform:uppercase;margin-top:0}
.svc{position:absolute;top:660px;width:195px;height:215px;background:#fff;box-shadow:0 2px 10px rgba(0,0,0,.12);text-align:center;padding-top:26px}
.svc svg{height:85px}
.svc h3{font-family:'Lato',sans-serif;font-weight:700;font-size:14px;color:#111;margin-top:14px}
.svc p{font-size:10px;line-height:15px;color:#444;margin:10px 14px 0}

/* about */
.about-photo{position:absolute;top:915px;height:513px}
.about-panel{position:absolute;left:267px;top:915px;width:673px;height:513px;background:var(--green);color:#fff;text-align:center;padding:56px 60px 0}
.about-panel h2{font-size:28px;text-transform:uppercase}
.about-panel .lead{font-size:17px;line-height:25px;margin-top:24px}
.about-panel .body{font-size:12px;line-height:19.5px;margin-top:24px}
.btn-deep{display:inline-block;background:var(--green-dark);color:#fff;font-size:11px;font-weight:900;padding:9px 25px;margin-top:32px;text-transform:uppercase}

/* vehicle park */
.section-title{position:absolute;width:1200px;text-align:center;color:var(--green);text-transform:uppercase}
.vp-card{position:absolute;top:1529px;width:212px;height:234px;box-shadow:0 6px 14px rgba(0,0,0,.2)}
.vp-feature{background:linear-gradient(180deg,#0d7a3b 0%,#2a8a4e 60%,#0b6a36 100%);color:#fff;padding:160px 0 0 18px}
.vp-feature h3{font-family:'Lato',sans-serif;font-weight:700;font-size:15px}
.btn-white{display:inline-block;background:#fff;color:var(--green);font-size:10px;padding:7px 14px;margin-top:11px}
.dots{position:absolute;display:flex;gap:5px}
.dots i{width:7px;height:7px;border-radius:50%;background:#111;display:block}
.dots i.on{background:var(--green)}

/* testimonials */
.testimonials{position:absolute;top:1846px;width:1200px;height:629px;background:radial-gradient(ellipse at 50% 40%,#f4f4f4 0%,var(--paper) 100%)}
.rule{position:absolute;left:578px;top:95px;width:36px;height:4px;background:var(--green)}
.polaroids{position:absolute;left:131px;top:145px;width:480px;height:401px;border-radius:45%;background:radial-gradient(ellipse,#cfcfcf 0%,#dcdcdc 60%,rgba(236,236,236,0) 72%)}
.polaroid{position:absolute;background:#fff;box-shadow:0 4px 12px rgba(0,0,0,.25);padding:20px 20px 60px}
.polaroid div{width:100%;height:100%}
.quote-mark{position:absolute;left:640px;top:220px;font-family:'Oswald',sans-serif;font-size:48px;color:var(--green);line-height:1}
.quote{position:absolute;left:640px;top:270px;width:330px;font-size:13px;line-height:20px;color:#666}
.author{position:absolute;left:640px;top:440px;font-family:'Oswald',sans-serif;font-size:17px;color:var(--green);text-transform:uppercase}

/* news */
.news-title{position:absolute;top:2505px;width:1200px;text-align:center;font-family:'Ubuntu',sans-serif;font-weight:500;font-size:29px;color:var(--green)}
.news{position:absolute;top:2573px;width:225px;height:363px;background:#fff;box-shadow:0 2px 10px rgba(0,0,0,.1)}
.news-img{height:222px}
.news h3{font-family:'Lato',sans-serif;font-weight:900;font-size:11px;color:#111;margin:20px 16px 0}
.news p{font-size:9px;line-height:15px;color:#777;margin:10px 16px 0}
.news .more{display:block;font-size:9px;font-weight:900;color:#111;margin:8px 16px 0}

/* cta */
.cta{position:absolute;top:2984px;width:1200px;height:245px;background:var(--green);color:#fff;text-align:center;padding-top:48px}
.cta h2{font-size:20px;text-transform:uppercase}
.cta p{font-size:12.5px;line-height:19.5px;width:560px;margin:14px auto 0}
.cta .btn-dark{margin-top:22px;padding:9px 15px}

/* footer */
.footer{position:absolute;top:3229px;width:1200px;height:334px;background:var(--footer);color:#fff}
.fcol{position:absolute;top:92px}
.fcol h4{font-size:12px;font-weight:700;margin-bottom:30px}
.fcol p{font-size:9px;line-height:18px}
.fcol ul{list-style:none}
.fcol li{font-size:10px;margin-bottom:18px}
.fcol li::before{content:"»";margin-right:12px}
.contact-row{display:flex;gap:10px}
.contact-row b{font-size:13px;font-weight:400;font-family:'Ubuntu',sans-serif;display:block;margin-bottom:10px}
.email{width:182px;height:30px;background:#fff;font-size:8px;color:#888;padding:10px 12px}
.send{display:inline-block;background:var(--green);font-size:10px;font-weight:700;padding:8px 24px;margin-top:16px}
.copy{position:absolute;left:252px;top:302px;font-size:8px}
.socials{position:absolute;left:856px;top:298px;display:flex;gap:6px}
.socials i{width:19px;height:19px;border-radius:50%;background:#fff;display:block}
</style>
</head>
<body>

<header class="hero">
  <div class="hero-truck" role="img" aria-label="Photo of a blue semi-trailer truck on a highway"></div>
  <div class="hero-road" role="img" aria-label="Sunlit desert road"></div>
  <div class="topbar">
    <div class="brand"><span class="brand-mark"></span><span class="brand-name">Brindle Works Australia</span></div>
    <nav class="nav">
      <span class="nav-tag">Mining &amp; Transport<br>Services</span>
      <ul><li>Home</li><li>Services</li><li>About us</li><li>Blog</li><li>Contacts</li></ul>
    </nav>
  </div>
  <div class="hero-copy">
    <h1>Services <span>Provider</span><br><span>in Australia</span></h1>
    <p>Lorem Ipsum is simply dummy text of the printing and typesetting has</p>
    <span class="btn-dark">Buy Transports</span>
  </div>
</header>

<section>
  <div class="services-head">
    <div class="kicker">MINING &amp; TRANSPORT</div>
    <h2>Services Provider in Australia</h2>
  </div>
  <div class="svc" style="left:282px">
    <svg viewBox="0 0 70 85" width="70"><defs><linearGradient id="g1" x1="0" y1="0" x2="0" y2="1"><stop offset="0" stop-color="#0b6a36"/><stop offset="1" stop-color="#6fae88"/></linearGradient></defs>
      <rect x="12" y="2" width="46" height="70" rx="6" fill="url(#g1)"/><rect x="18" y="10" width="34" height="22" fill="#fff"/><rect x="24" y="42" width="22" height="14" fill="#fff"/><rect x="2" y="28" width="6" height="14" fill="url(#g1)"/><rect x="62" y="28" width="6" height="14" fill="url(#g1)"/><rect x="16" y="72" width="10" height="10" fill="url(#g1)"/><rect x="44" y="72" width="10" height="10" fill="url(#g1)"/></svg>
    <h3>Transport</h3>
    <p>Lorem Ipsum is simply dummy text of the printing and typesetting</p>
  </div>
  <div class="svc" style="left:502px">
    <svg viewBox="0 0 115 85" width="115"><defs><linearGradient id="g2" x1="0" y1="0" x2="0" y2="1"><stop offset="0" stop-color="#0b6a36"/><stop offset="1" stop-color="#6fae88"/></linearGradient></defs>
      <rect x="20" y="20" width="40" height="28" fill="url(#g2)"/><rect x="28" y="26" width="14" height="12" fill="#fff"/><rect x="8" y="50" width="70" height="16" rx="8" fill="url(#g2)"/><path d="M80 36 L108 62 L96 66 L78 50Z" fill="url(#g2)"/><rect x="62" y="32" width="16" height="16" fill="url(#g2)"/></svg>
    <h3>Earthmoving</h3>
    <p>Lorem Ipsum is simply dummy text of the printing and typesetting</p>
  </div>
  <div class="svc" style="left:722px">
    <svg viewBox="0 0 90 85" width="90"><defs><linearGradient id="g3" x1="0" y1="0" x2="0" y2="1"><stop offset="0" stop-color="#0b6a36"/><stop offset="1" stop-color="#6fae88"/></linearGradient></defs>
      <path d="M4 82 V46 L24 34 V46 L44 34 V46 L60 36 V14 H72 V82Z" fill="url(#g3)"/><rect x="54" y="2" width="32" height="10" rx="5" fill="url(#g3)"/><rect x="12" y="56" width="8" height="7" fill="#fff"/><rect x="26" y="56" width="8" height="7" fill="#fff"/><rect x="40" y="56" width="8" height="7" fill="#fff"/><rect x="12" y="68" width="8" height="7" fill="#fff"/><rect x="26" y="68" width="8" height="7" fill="#fff"/><rect x="40" y="68" width="8" height="7" fill="#fff"/></svg>
    <h3>Industrial</h3>
    <p>Lorem Ipsum is simply dummy text of the printing and typesetting</p>
  </div>
</section>

<section>
  <div class="about-photo" style="left:0;width:267px;background:linear-gradient(180deg,#8fb6cc 0%,#b23a3a 45%,#6a6e74 100%)" role="img" aria-label="Photo of a red truck on a road"></div>
  <div class="about-panel">
    <h2>About Brindle Works Australia</h2>
    <p class="lead">Lorem Ipsum is simply dummy text of the printing and typesetting Lorem Ipsum has been the industry's standard dummy</p>
    <p class="body">Lorem Ipsum is simply dummy text of the printing and typesetting industry. Lorem Ipsum has been the industry's standard dummy text ever since the 1500s, when an unknown printer took a galley of type and scrambled it to make a type specimen book. It has survived not only five centuries, but also the leap into electronic typesetting, remaining essentially unchanged. It was popularised in the 1960s with the release of Letraset sheets containing Lorem Ipsum passages, and more recently with desktop publishing software like Aldus PageMaker including versions of Lorem Ipsum.a</p>
    <p class="body" style="margin-top:18px">Lorem Ipsum is simply dummy text of the printing and typesetting industry. Lorem Ipsum has been the industry's standard dummy text ever since the 1500s, when an unknown printer took a galley of type and scrambled it to make a type specimen book. It has survived not only five centuries, but also the leap into electronic typesetting, remaining essentially unchanged.</p>
    <span class="btn-deep">Read more</span>
  </div>
  <div class="about-photo" style="left:940px;width:260px;background:linear-gradient(180deg,#c9a21c 0%,#e2b820 35%,#5a5a55 70%,#9a9a96 100%)" role="img" aria-label="Photo of a yellow mining dump truck"></div>
</section>

<section>
  <h2 class="section-title" style="top:1462px;font-size:29px">Vehicle Park</h2>
  <div class="vp-card" style="left:249px;background:linear-gradient(135deg,#8aa0b4 0%,#2f4452 55%,#1c2630 100%)" role="img" aria-label="Close-up photo of a truck wheel"></div>
  <div class="vp-card vp-feature" style="left:495px"><h3>Transport Services</h3><span class="btn-white">Buy Transport</span></div>
  <div class="vp-card" style="left:740px;background:linear-gradient(180deg,#0e2a8a 0%,#2a55b8 60%,#1a1d24 100%)" role="img" aria-label="Photo of an oil pump jack against blue sky"></div>
  <div class="dots" style="left:585px;top:1796px"><i></i><i class="on"></i><i></i></div>
</section>

<section class="testimonials">
  <h2 class="section-title" style="top:46px;font-size:29px">Testimonials</h2>
  <div class="rule"></div>
  <div class="polaroids" role="img" aria-label="Stack of instant photos with a customer portrait"></div>
  <div class="polaroid" style="left:205px;top:260px;width:170px;height:220px;transform:rotate(-8deg)"><div style="background:#9a8a6a"></div></div>
  <div class="polaroid" style="left:460px;top:240px;width:155px;height:220px;transform:rotate(6deg)"><div style="background:#2e4a8a"></div></div>
  <div class="polaroid" style="left:270px;top:215px;width:250px;height:265px;transform:rotate(-5deg)"><div style="background:#6c7f8a"></div></div>
  <div class="polaroid" style="left:280px;top:230px;width:250px;height:265px;transform:rotate(-12deg)"><div style="background:linear-gradient(160deg,#6a6a6a,#9aa9b8)" role="img" aria-label="Portrait of a smiling customer"></div></div>
  <div class="dots" style="left:384px;top:524px"><i style="width:4px;height:4px;background:#333"></i><i style="width:4px;height:4px;background:#333"></i><i style="width:6px;height:6px;background:none;border:1px solid var(--green)"></i><i style="width:4px;height:4px;background:#333"></i></div>
  <div class="quote-mark">“</div>
  <p class="quote">Lorem Ipsum is simply dummy text of the printing and typesetting industry. Lorem Ipsum has been the industry's standard dummy text ever since the 1500s, when an unknown printer took a galley of type and scrambled it to make a type specimen book. It has survived not only five centuries, but also the leap into electronic typesetting, remaining essentially unchanged.</p>
  <div class="author">Marcus Hale</div>
</section>

<section>
  <h2 class="news-title">Latest News</h2>
  <article class="news" style="left:250px">
    <div class="news-img" style="background:linear-gradient(180deg,#9cc3e6 0%,#d8c25a 45%,#7c5a3a 75%,#3a6a8a 100%)" role="img" aria-label="Photo of a container ship at a port"></div>
    <h3>LOREM IPSUM IS SIMPLY DUMMY</h3>
    <p>Lorem Ipsum is simply dummy text of the printing and typesetting industry. Lorem Ipsum has been the industry's standard dummy text ever since the</p>
    <span class="more">READ MORE</span>
  </article>
  <article class="news" style="left:490px">
    <div class="news-img" style="background:linear-gradient(135deg,#4a5d78 0%,#2a2f38 60%,#b89a86 100%)" role="img" aria-label="Photo of a driver's hand on a gear stick"></div>
    <h3>LOREM IPSUM IS SIMPLY DUMMY</h3>
    <p>Lorem Ipsum is simply dummy text of the printing and typesetting industry. Lorem Ipsum has been the industry's standard dummy text ever since the</p>
    <span class="more">READ MORE</span>
  </article>
  <article class="news" style="left:729px">
    <div class="news-img" style="background:linear-gradient(135deg,#d6d8da 0%,#9aa0a6 45%,#e8962a 75%,#3a3a3a 100%)" role="img" aria-label="Photo of a worker holding an orange clipboard by a truck"></div>
    <h3>LOREM IPSUM IS SIMPLY DUMMY</h3>
    <p>Lorem Ipsum is simply dummy text of the printing and typesetting industry. Lorem Ipsum has been the industry's standard dummy text ever since the</p>
    <span class="more">READ MORE</span>
  </article>
</section>

<section class="cta">
  <h2>Reach your destination 100% sure and safe</h2>
  <p>Lorem Ipsum is simply dummy text of the printing and typesetting industry. Lorem Ipsum has been the industry's standard dummy text ever since the 1500s, when an unknown printer took a galley of type and scrambled it to make a type specimen book. It has survived not only five centuries, but also the leap into electronic typesetting, remaining essentially unchanged.</p>
  <span class="btn-dark">Buy Transports</span>
</section>

<footer class="footer">
  <div class="fcol" style="left:252px;width:185px">
    <h4>About us</h4>
    <p>Lorem Ipsum is simply dummy text of the printing and typesetting industry. standard dummy text ever since the 1500s, when an unknown printer took a galley of type and scrambled it to make a type specimen book. It has survived not only five centuries,</p>
  </div>
  <div class="fcol" style="left:459px;width:180px">
    <h4>Contact us</h4>
    <div class="contact-row">
      <svg width="12" height="16" viewBox="0 0 12 16"><path d="M6 0a6 6 0 0 1 6 6c0 4-6 10-6 10S0 10 0 6a6 6 0 0 1 6-6z" fill="#0b6a36"/><circle cx="6" cy="6" r="2.2" fill="#0d0d0d"/></svg>
      <div><b>Address:</b><p>Abc Street City #12345 simply dummy text of the printing and typesetting</p></div>
    </div>
    <div class="contact-row" style="margin-top:14px">
      <svg width="12" height="12" viewBox="0 0 12 12"><path d="M2 0l3 3-1.5 2a7 7 0 0 0 3.5 3.5L9 7l3 3-2 2C5 12 0 7 0 2z" fill="#0b6a36"/></svg>
      <div><b>Phone:</b><p>(123)456-6789</p></div>
    </div>
  </div>
  <div class="fcol" style="left:658px">
    <h4>User area</h4>
    <ul><li>Home</li><li>Services</li><li>About us</li><li>Blog</li><li>Contacts</li></ul>
  </div>
  <div class="fcol" style="left:770px">
    <h4>Subscribe to Newsletters</h4>
    <div class="email">Your Email Address</div>
    <span class="send">Send</span>
  </div>
  <div class="copy">Copyright 2020 <b>Brindle Works Australia</b>. All Right Reserved.</div>
  <div class="socials"><i></i><i></i><i></i><i></i></div>
</footer>

</body>
</html>
```